Product Description page for Hullwrap.com, References here just need a clean up redesign

Hi, were working on updating the product description page of our site hullwrap.com

Attached is a reference of what we drew on paint. We want to keep it pretty much the same as far as whats on there, the components with a few small adjustments and a clean actually designed look.

1. We want to remove the tabs (product description, warranty, reviews) and put it all in that main content area stretching down into sections. IE: Product Description section, followed by reviews, followed by warranty, below each other.
2. The side bar needs to be redesigned as far as the look and feel but the content and whats in there should stay the same.
3. The main banner area will be replaced shortly you do not have to worry about that.
4. Include a section or box for people to put in their email for a free Ebook.

Target Market(s)

people looking to easily view our boat cover products and buy without having to click too often or leave the page.

Industry/Entity Type

Online Shopping

Number of Pages Required

1 page

Requirements
Must have
• - Must update the sidebar
• - Must update the content area to remove the tabs and put the content from each tab sectioned off below each other (dummy text is fine for now for the tabs you cant view)
Nice to have
• - Cool place thats clean and functional to insert a section for people to put in their email to receive a free ebook
Should not have
• - too much change, we already know what we want and have a solid reference to work from.

```html
<!DOCTYPE html>
<html lang="en">
<head>
<meta charset="utf-8">
<title>Hullwrap.com – Product Page</title>
<link href="https://fonts.googleapis.com/css2?family=Open+Sans:wght@400;600;700&family=Roboto:wght@400;500;700&family=Roboto+Condensed:wght@400;700&display=swap" rel="stylesheet">
<style>
:root{
  --yellow:#f6b71b;
  --blue:#1f5aa8;
  --blue-dark:#174a8d;
  --ink:#222;
  --muted:#666;
  --line:#dcdcdc;
  --panel:#e2e2e2;
  --footer:#1c1c1c;
  --orange:#f39c12;
  --price:#2a6fb8;
}
*{box-sizing:border-box;margin:0;padding:0}
html,body{width:1200px;height:2830px;overflow:hidden;background:#fff}
body{position:relative;font-family:"Roboto",Arial,sans-serif;color:var(--ink)}
.abs{position:absolute}

/* top strip */
.topbar{left:0;top:0;width:1200px;height:34px;background:var(--yellow);font-size:13px;color:#2b2b2b;display:flex;justify-content:space-between;align-items:center;padding:0 60px 0 66px}

/* header */
.brand{left:60px;top:58px;display:flex;align-items:center;gap:10px}
.brand-dot{width:46px;height:46px;border-radius:50%;background:var(--yellow)}
.brand-name{font-family:"Open Sans",sans-serif;font-weight:700;font-size:38px;color:var(--blue);letter-spacing:-.5px}
.callbox{left:836px;top:63px;width:306px;height:40px;border:1px solid var(--line);display:flex;align-items:center;gap:10px;padding-left:4px}
.callbox .ico{width:28px;height:28px;background:var(--blue);border-radius:3px;display:flex;align-items:center;justify-content:center}
.callbox .lbl{font-size:16px;font-weight:700;color:var(--blue)}
.callbox .num{font-size:21px;color:var(--yellow);font-weight:500}

/* nav */
.nav{left:60px;top:132px;width:1080px;height:49px;background:var(--blue);display:flex;align-items:center}
.nav a{color:#fff;font-weight:700;font-size:15px;text-decoration:none;margin-left:24px;margin-right:26px}
.nav .checkout{position:absolute;right:0;top:0;height:49px;width:212px;background:var(--blue-dark);display:flex;align-items:center;gap:12px;padding-left:22px;color:#fff;font-weight:700;font-size:15px}
.cart-count{width:30px;height:30px;border-radius:50%;background:var(--yellow);font-size:14px;display:flex;align-items:center;justify-content:center}

/* hero */
.hero{left:0;top:181px;width:1200px;height:545px;background:linear-gradient(180deg,#3c4650 0%,#2a2f33 45%,#1c1e20 100%)}
.hero-title{left:0;top:326px;width:1200px;text-align:center;font-family:"Open Sans",sans-serif;font-weight:700;font-size:54px;color:var(--yellow)}
.hero-sub{left:0;top:402px;width:1200px;text-align:center;font-size:23px;color:#fff;letter-spacing:.3px}
.finder{left:211px;top:462px;width:785px;height:70px;background:rgba(255,255,255,.35);border-radius:4px;padding:6px;display:flex;gap:0}
.finder .sel{background:#eee;height:58px;display:flex;align-items:center;justify-content:space-between;padding:0 20px;font-size:19px;color:#888;border-right:1px solid #ccc}
.finder .go{background:var(--blue);color:#fff;font-weight:600;font-size:20px;height:58px;display:flex;align-items:center;justify-content:center;width:222px;font-family:"Open Sans",sans-serif}
.caret{width:0;height:0;border-left:6px solid transparent;border-right:6px solid transparent;border-top:7px solid #555}

/* boat styles */
.styles{left:0;top:726px;width:1200px;height:246px;background:var(--panel)}
.styles h2{position:absolute;left:0;top:44px;width:1200px;text-align:center;font-weight:400;font-size:27px;color:#555;font-family:"Open Sans",sans-serif}
.style-card{position:absolute;top:110px;height:102px;background:#fff;display:flex;flex-direction:column;align-items:center;justify-content:flex-end;padding-bottom:14px;font-size:11px;color:#333;letter-spacing:.2px}
.style-card .pic{width:100px;height:40px;margin-bottom:14px;background:linear-gradient(180deg,#cfd2d6,#8d939a);border-radius:20px 20px 6px 6px}

/* product */
.fitbar{left:70px;top:1019px;width:1060px;height:53px;background:var(--blue);border-radius:3px;color:#fff;font-size:21px;display:flex;align-items:center;padding-left:16px}
.fitbar .arr{position:absolute;top:14px;width:34px;height:26px;display:flex;align-items:center;justify-content:center}
.mainimg{left:79px;top:1108px;width:430px;height:226px;border:1px solid var(--line);padding:14px}
.mainimg .ph{width:100%;height:100%;background:linear-gradient(180deg,#fff 0%,#c8cbce 45%,#8e949a 70%,#f1f1f1 100%)}
.thumbs{left:79px;top:1340px;width:430px;height:68px;border:1px solid var(--line);background:#f5f5f5;display:flex;align-items:center;gap:12px;padding-left:38px}
.thumbs span{width:58px;height:58px}
.ptitle{left:542px;top:1106px;font-family:"Open Sans",sans-serif;font-size:33px;color:#222}
.stars{display:flex;gap:2px}
.oldp{left:548px;top:1207px;font-size:26px;color:#999;text-decoration:line-through}
.newp{left:624px;top:1201px;font-size:36px;color:var(--price)}
.field-l{font-size:17px;color:#444}
.optsel{left:630px;top:1257px;width:192px;height:42px;border:1px solid #ccc;display:flex;align-items:center;justify-content:space-between;padding:0 14px;font-size:16px;color:#666}
.qty{left:630px;top:1316px;width:66px;height:42px;border:1px solid #ccc;font-size:16px;padding:10px}
.addcart{left:549px;top:1372px;width:162px;height:41px;background:var(--yellow);border-radius:3px;font-weight:500;font-size:17px;display:flex;align-items:center;justify-content:center}
.ship{font-family:"Roboto Condensed",sans-serif;font-style:italic;font-size:12px;color:#3a6b2a;display:flex;align-items:center;gap:5px}

/* related */
.related{left:0;top:1485px;width:1200px;height:479px;background:linear-gradient(180deg,#262626,#1a1a1a)}
.rcard{position:absolute;top:1532px;width:308px;height:374px;background:#e8e8e8;overflow:hidden}
.rcard .ph{position:absolute;left:14px;top:16px;width:280px;height:180px;background:#fff}
.rcard .ph i{position:absolute;left:20px;top:44px;width:240px;height:96px;border-radius:60px 80px 20px 20px}
.rcard .ribbon{position:absolute;left:-46px;top:26px;width:170px;height:30px;background:var(--blue);transform:rotate(-45deg);color:#fff;font-weight:700;font-size:14px;text-align:center;line-height:30px}
.rcard .name{position:absolute;left:0;top:212px;width:308px;text-align:center;font-family:"Open Sans",sans-serif;font-size:19px;line-height:24px;color:#333}
.rcard .from{position:absolute;top:282px;left:58px;font-size:14px;color:#333}
.rcard .amt{position:absolute;top:268px;left:104px;font-size:33px;color:var(--price);font-weight:500}
.rcard .meta{position:absolute;left:14px;top:342px;width:280px;display:flex;justify-content:space-between;align-items:center}

/* content sections */
.sec-h{height:37px;background:var(--panel);font-family:"Open Sans",sans-serif;font-size:21px;color:#222;padding-left:10px;display:flex;align-items:center}
.desc{left:95px;top:2057px;width:1010px;font-size:13.6px;line-height:24px;color:#333}
.scale{left:92px;top:2242px;width:538px;height:14px;display:flex}
.scale span{flex:1;color:#fff;font-size:9px;text-align:center;line-height:14px}
.rrow{left:92px;width:538px;font-size:12px;color:#333}
.rrow .v{position:absolute;right:0;top:0}
.rrow .track{position:absolute;left:0;top:17px;width:538px;height:4px;background:#e3e3e3}
.rrow .fill{position:absolute;left:0;top:0;height:4px}
.warranty{left:688px;top:2236px;font-size:14px;color:#333}

/* footer */
.footer{left:0;top:2517px;width:1200px;height:313px;background:var(--footer)}
.fbadge{left:98px;top:2485px;width:192px;height:327px}
.fbadge .txt{position:absolute;left:14px;top:60px;width:170px;color:#fff;font-size:13px;line-height:24px}
.fbadge .bname{font-family:"Open Sans",sans-serif;font-weight:700;font-size:22px;color:#fff;margin-bottom:8px}
.fcol h3{font-weight:700;font-size:18px;color:#fff;margin-bottom:20px}
.fcol p{font-size:12px;line-height:19px;color:#ddd}
.nl-row{display:flex;align-items:center;gap:10px;margin-bottom:16px;color:#fff;font-size:14px;font-weight:700}
.nl-row span{width:46px}
.nl-row i{display:block;width:210px;height:27px;background:#fff}
.subscribe{margin-left:156px;width:108px;height:30px;background:var(--yellow);color:#222;font-size:14px;display:flex;align-items:center;justify-content:center}
.social{display:flex;gap:14px;margin-top:22px}
.social i{width:26px;height:26px;border-radius:50%;display:block}
.copyright{left:334px;top:2768px;font-size:13px;color:#ccc}
</style>
</head>
<body>

<div class="abs topbar"><span>Store Hours(M-F, 9:30AM - 6PM PST)</span><span>218 Marina Point Road, Cedar Bay NY 10980</span></div>

<div class="abs brand"><span class="brand-dot"></span><span class="brand-name">Hullwrap.com</span></div>
<div class="abs callbox">
  <span class="ico"><svg width="16" height="16" viewBox="0 0 24 24"><path fill="#fff" d="M6.6 10.8a15 15 0 0 0 6.6 6.6l2.2-2.2c.3-.3.7-.4 1-.2 1.1.4 2.3.6 3.6.6.6 0 1 .4 1 1V20c0 .6-.4 1-1 1A17 17 0 0 1 3 4c0-.6.4-1 1-1h3.5c.6 0 1 .4 1 1 0 1.3.2 2.5.6 3.6.1.3 0 .7-.2 1z"/></svg></span>
  <span class="lbl">CALL US ON:</span><span class="num">(800) 555-0192</span>
</div>

<nav class="abs nav">
  <a>Boat Covers</a><a>Bass Boat Covers</a><a>T Top Boat Covers</a><a>Bimini Tops</a><a>Jet Ski Covers</a>
  <div class="checkout">Checkout <span class="caret" style="border-top-color:#fff"></span>
    <svg width="30" height="26" viewBox="0 0 30 26"><path d="M1 2h5l4 15h14l3-10H8" fill="none" stroke="#fff" stroke-width="3"/><circle cx="12" cy="22" r="2.5" fill="#fff"/><circle cx="22" cy="22" r="2.5" fill="#fff"/></svg>
    <span class="cart-count">0</span></div>
</nav>

<div class="abs hero" role="img" aria-label="Photo of a covered boat on a trailer beside a lake"></div>
<div class="abs hero-title">Can't Find Your Boat ?</div>
<div class="abs hero-sub">CHAT WITH US NOW NOW AND WE'LL HELP YOU FIND IT IN NO TIME!</div>
<div class="abs finder">
  <div class="sel" style="width:122px">Year <span class="caret"></span></div>
  <div class="sel" style="width:212px">Please Select.... <span class="caret"></span></div>
  <div class="sel" style="width:222px;border-right:none">Please Select.... <span class="caret"></span></div>
  <div class="go">VIEW COVERS NOW</div>
</div>
<svg class="abs" style="left:576px;top:656px" width="50" height="28" viewBox="0 0 50 28"><path d="M2 2l23 22L48 2" fill="none" stroke="#fff" stroke-width="3"/></svg>

<section class="abs styles">
  <h2>SEARCH BY BOAT STYLE &amp; SIZE</h2>
  <svg style="position:absolute;left:26px;top:138px" width="14" height="22"><path d="M12 2L3 11l9 9" fill="none" stroke="#444" stroke-width="3"/></svg>
  <svg style="position:absolute;left:1158px;top:138px" width="14" height="22"><path d="M2 2l9 9-9 9" fill="none" stroke="#444" stroke-width="3"/></svg>
  <div class="style-card" style="left:68px;width:142px"><span class="pic" role="img" aria-label="Pro bass boat drawing"></span>PRO BASS BOAT</div>
  <div class="style-card" style="left:230px;width:180px"><span class="pic" role="img" aria-label="Runabout boat drawing"></span>RUNABOUT WITH BOW RAILS</div>
  <div class="style-card" style="left:432px;width:190px"><span class="pic" role="img" aria-label="Performance boat drawing"></span>PERFORMANCE BOATS I/O</div>
  <div class="style-card" style="left:643px;width:178px"><span class="pic" role="img" aria-label="Performance boat outboard drawing"></span>PERFORMANCE BOATS O/B</div>
  <div class="style-card" style="left:842px;width:143px"><span class="pic" role="img" aria-label="Inflatable boat drawing"></span>INFLATABLE BOAT</div>
  <div class="style-card" style="left:996px;width:134px"><span class="pic" role="img" aria-label="Jet boat drawing"></span>JET BOAT</div>
</section>

<div class="abs fitbar">Fits: Center Console with Bow Rails Up to 16'8" Long &amp; 90" Wide
  <span class="arr" style="left:966px;background:var(--yellow)"><svg width="10" height="14"><path d="M8 1L2 7l6 6" fill="none" stroke="#333" stroke-width="2"/></svg></span>
  <span class="arr" style="left:1012px;background:#9a9a9a"><svg width="10" height="14"><path d="M2 1l6 6-6 6" fill="none" stroke="#333" stroke-width="2"/></svg></span>
</div>

<div class="abs mainimg"><div class="ph" role="img" aria-label="Grey boat cover fitted on a boat and trailer"></div></div>
<div class="abs thumbs">
  <svg style="position:absolute;left:12px;top:26px" width="10" height="16"><path d="M8 1L2 8l6 7" fill="none" stroke="#777" stroke-width="2"/></svg>
  <span role="img" aria-label="Cover storage bag" style="background:#d9d3c8"></span>
  <span role="img" aria-label="Blue fabric swatch" style="background:#2e64a8"></span>
  <span role="img" aria-label="Cover strap detail" style="background:#6f6f73"></span>
  <span role="img" aria-label="Tie-down detail" style="background:#4a4a4c"></span>
  <span role="img" aria-label="Buckle detail" style="background:#3a3a3c"></span>
  <svg style="position:absolute;right:10px;top:26px" width="10" height="16"><path d="M2 1l6 7-6 7" fill="none" stroke="#777" stroke-width="2"/></svg>
</div>

<div class="abs ptitle">Harborline Tidal Custom Cover</div>
<div class="abs" style="left:542px;top:1162px;display:flex;align-items:center;gap:14px">
  <svg width="132" height="24" viewBox="0 0 132 24">
    <g id="s"><path d="M12 1l3.4 7 7.6 1-5.5 5.3 1.3 7.6L12 18.3 5.2 21.9l1.3-7.6L1 9l7.6-1z"/></g>
    <path fill="#f3a21c" d="M12 1l3.4 7 7.6 1-5.5 5.3 1.3 7.6L12 18.3 5.2 21.9l1.3-7.6L1 9l7.6-1z"/>
    <path fill="#f3a21c" transform="translate(26 0)" d="M12 1l3.4 7 7.6 1-5.5 5.3 1.3 7.6L12 18.3 5.2 21.9l1.3-7.6L1 9l7.6-1z"/>
    <path fill="#f3a21c" transform="translate(52 0)" d="M12 1l3.4 7 7.6 1-5.5 5.3 1.3 7.6L12 18.3 5.2 21.9l1.3-7.6L1 9l7.6-1z"/>
    <path fill="#c8c8c8" transform="translate(78 0)" d="M12 1l3.4 7 7.6 1-5.5 5.3 1.3 7.6L12 18.3 5.2 21.9l1.3-7.6L1 9l7.6-1z"/>
    <path fill="#c8c8c8" transform="translate(104 0)" d="M12 1l3.4 7 7.6 1-5.5 5.3 1.3 7.6L12 18.3 5.2 21.9l1.3-7.6L1 9l7.6-1z"/>
  </svg>
  <span style="font-size:17px;color:#777;font-style:italic">(27 Reviews)</span>
</div>
<div class="abs oldp">$179</div>
<div class="abs newp">$179</div>
<div class="abs field-l" style="left:549px;top:1267px">Colour:</div>
<div class="abs optsel">Choose an Options <span class="caret"></span></div>
<div class="abs" style="left:840px;top:1259px;width:40px;height:40px;background:var(--blue)"></div>
<div class="abs" style="left:894px;top:1259px;width:40px;height:40px;background:#8e8e8e"></div>
<div class="abs field-l" style="left:549px;top:1324px">Quantity:</div>
<div class="abs qty">1</div>
<div class="abs addcart">Add to Cart</div>
<div class="abs ship" style="left:736px;top:1386px"><svg width="16" height="10" viewBox="0 0 16 10"><rect x="0" y="1" width="10" height="6" fill="#3a6b2a"/><path d="M10 3h3l2 3v1h-5z" fill="#3a6b2a"/><circle cx="3" cy="8.5" r="1.5" fill="#3a6b2a"/><circle cx="12" cy="8.5" r="1.5" fill="#3a6b2a"/></svg>Free Shipping!</div>

<section class="abs related" role="img" aria-label="Dark photo backdrop of a covered boat"></section>

<div class="rcard" style="left:77px">
  <div class="ph" role="img" aria-label="Sports car with beige car cover"><i style="background:linear-gradient(180deg,#d8cdb0 0%,#c9bc98 55%,#6b6d70 56%,#3e4043 100%)"></i></div>
  <div class="ribbon">ON SALE</div>
  <div class="name">Harborline Series 4 Custom<br>Car Cover</div>
  <div class="from">From</div><div class="amt">$152.00</div>
  <div class="meta"><span class="ship">Free Shipping!</span><span style="font-size:12px;color:#f3a21c">★★★<span style="color:#bbb">★★</span> <span style="color:#333">(1K+)</span></span></div>
</div>
<div class="rcard" style="left:446px">
  <div class="ph" role="img" aria-label="Red sports car with grey car cover"><i style="background:linear-gradient(180deg,#bfc2c5 0%,#a7abaf 40%,#d3212b 41%,#8e1218 100%)"></i></div>
  <div class="ribbon">ON SALE</div>
  <div class="name">Harborline Series 4 Custom<br>Car Cover</div>
  <div class="from">From</div><div class="amt">$152.00</div>
  <div class="meta"><span class="ship">Free Shipping!</span><span style="font-size:12px;color:#f3a21c">★★★<span style="color:#bbb">★★</span> <span style="color:#333">(1K+)</span></span></div>
</div>
<div class="rcard" style="left:814px">
  <div class="ph" role="img" aria-label="Sports car with beige car cover"><i style="background:linear-gradient(180deg,#d8cdb0 0%,#c9bc98 55%,#6b6d70 56%,#3e4043 100%)"></i></div>
  <div class="ribbon">ON SALE</div>
  <div class="name">Harborline Series 4 Custom<br>Car Cover</div>
  <div class="from">From</div><div class="amt">$152.00</div>
  <div class="meta"><span class="ship">Free Shipping!</span><span style="font-size:12px;color:#f3a21c">★★★<span style="color:#bbb">★★</span> <span style="color:#333">(1K+)</span></span></div>
</div>

<div class="abs sec-h" style="left:87px;top:2000px;width:1021px">Product Description:</div>
<p class="abs desc">Lorem Ipsum is simply dummy text of the printing and typesetting industry. Lorem Ipsum has been the industry's standard dummy text ever since the 1500s, when an unknown printer took a galley of type and scrambled it to make a type specimen book. It has survived not only five centuries, but also the leap into electronic typesetting, remaining essentially unchanged.</p>

<div class="abs sec-h" style="left:87px;top:2172px;width:549px">Reviews:</div>
<div class="abs sec-h" style="left:676px;top:2172px;width:428px">Warranty:</div>

<div class="abs scale">
  <span style="background:#163a63">1</span><span style="background:#1b5e5a">2</span><span style="background:#2f7d3b">3</span><span style="background:#5f9e2f">4</span><span style="background:#9cbc2a">5</span><span style="background:#e4c51d">6</span><span style="background:#f2a91c">7</span><span style="background:#f28a1d">8</span><span style="background:#ee6a1f">9</span><span style="background:#e8401f">10</span>
</div>
<div class="abs rrow" style="top:2272px">Desing<span class="v">10</span><span class="track"><span class="fill" style="width:538px;background:#ee5a24"></span></span></div>
<div class="abs rrow" style="top:2305px">Display Quality<span class="v">5</span><span class="track"><span class="fill" style="width:269px;background:#f4b41a"></span></span></div>
<div class="abs rrow" style="top:2339px">Software<span class="v">8</span><span class="track"><span class="fill" style="width:430px;background:#f27b1e"></span></span></div>
<div class="abs rrow" style="top:2373px">Accessories<span class="v">8</span><span class="track"><span class="fill" style="width:430px;background:#f27b1e"></span></span></div>

<p class="abs warranty">1 year manufacturer warranty for Hullwrap.</p>

<footer class="abs footer"></footer>
<div class="abs fbadge">
  <svg width="192" height="327" viewBox="0 0 192 327" style="position:absolute;left:0;top:0"><path d="M0 0h176l16 22v305l-96-36L0 327z" fill="#2463b5"/></svg>
  <span style="position:absolute;left:80px;top:22px;width:26px;height:26px;border-radius:50%;background:#fff"></span>
  <div class="txt"><div class="bname">Hullwrap.com</div>
    218 Marina Point Road,<br>Cedar Bay NY 10980<br><br>
    <span style="padding-left:12px">+1-888-555-0147</span><br><br>
    <span style="padding-left:12px;font-size:12px">contact@hullwrap.com</span></div>
</div>

<div class="abs fcol" style="left:334px;top:2566px;width:200px">
  <h3>About Us</h3>
  <p>Lorem Ipsum is simply dummy text of the printing and typesetting industry. Lorem Ipsum has been the industry's standard dummy text ever since the 1500s.</p>
</div>
<div class="abs fcol" style="left:576px;top:2566px;width:270px">
  <h3>Subscribe Newsletter</h3>
  <div class="nl-row"><span>Name</span><i></i></div>
  <div class="nl-row"><span>Email</span><i></i></div>
  <div class="subscribe">Subscribe</div>
</div>
<div class="abs fcol" style="left:883px;top:2568px;width:230px">
  <p style="color:#fff">For Special booking request, Please Call</p>
  <div style="font-size:31px;color:var(--yellow);margin-top:14px">(800) 555-0192</div>
  <div class="social"><i style="background:#3fa9e0"></i><i style="background:#d8334b"></i><i style="background:#3b5ca0"></i><i style="background:#d7362c"></i></div>
</div>
<div class="abs copyright">Copyright © 2016  Hullwrap.com. All Rights Reserved</div>

</body>
</html>
```